Brochure

I have a current booklet for Cedar Ridge Labs, I need to incorporate additional information and testing into it. attached are the current inside pages and the additional items that need to be added.

Requirements
Must have
• matching the background, colors, and format of the original inside booklet pages.

```html
<!DOCTYPE html>
<html lang="en">
<head>
<meta charset="utf-8">
<title>Cedar Ridge Labs – Testing Panels</title>
<link href="https://fonts.googleapis.com/css2?family=Poppins:wght@400;500;600;700&display=swap" rel="stylesheet">
<style>
:root{
  --stage:#6b6b6b;
  --paper:#ffffff;
  --brand:#1f74c6;
  --brand-bright:#2f8be0;
  --band:#595959;
  --ink:#1d1d1d;
  --tick:#1f74c6;
}
*{box-sizing:border-box;margin:0;padding:0}
html,body{width:1021px;height:1200px;overflow:hidden}
body{background:var(--stage);font-family:"Poppins",sans-serif;color:var(--ink);position:relative}
.page{position:absolute;width:362px;height:469px;background:var(--paper);box-shadow:0 3px 10px rgba(0,0,0,.35);overflow:hidden}
.page--abr{left:112px;top:98px}
.page--nail{left:548px;top:98px}
.page--uti{left:112px;top:634px}
.page--wound{left:548px;top:634px}
.hero{position:absolute;left:0;top:0;width:362px;z-index:0}
.brand-mark{position:absolute;left:22px;top:36px;display:flex;align-items:center;gap:5px;color:#fff;font-weight:600;font-size:11px;line-height:1.1;width:110px;z-index:1}
.brand-mark .dot{width:10px;height:10px;border-radius:50%;background:#fff;flex:none}
.page-title{position:absolute;left:20px;font-size:12.5px;font-weight:600;letter-spacing:.1px;color:#333;z-index:1}
.page-title span{color:var(--brand)}
.features{position:absolute;left:20px;width:330px;display:grid;grid-template-columns:165px 165px;row-gap:9px;z-index:1}
.feature{display:flex;align-items:center;gap:9px;font-size:7.5px;line-height:1.25}
.feature svg{width:22px;height:22px;flex:none}
.feature b{font-weight:600}
.band{position:absolute;left:0;width:362px;background:var(--band);color:#fff;padding:4px 20px 5px;z-index:1}
.band h2{font-size:13px;font-weight:700;color:var(--brand-bright);line-height:1.15}
.band p{font-size:7.2px;line-height:1.3}
.content{position:absolute;left:20px;right:20px}
.section-head{font-size:9.5px;font-weight:600;color:var(--brand);line-height:1.2}
.list{list-style:none}
.list li{font-size:6.3px;line-height:11.2px;display:flex;align-items:center;gap:4px;white-space:nowrap}
.list li::before{content:"";width:5px;height:5px;border-radius:50%;background:var(--tick);flex:none;
  background-image:linear-gradient(45deg,transparent 40%,#fff 40%,#fff 55%,transparent 55%);}
.small-note{font-size:4.8px;line-height:1.3}
.photo{border:1.5px solid #8a8a8a}
.pagenum{position:absolute;right:28px;bottom:16px;width:7px;height:7px;border-radius:50%;background:var(--brand-bright)}
</style>
</head>
<body>

<!-- Page 1: Antibiotic Resistance Gene -->
<section class="page page--abr">
  <svg class="hero" height="246" viewBox="0 0 362 246">
    <polygon points="175,0 362,0 362,205 110,82" fill="#2aa6d8" role="img" aria-label="Microscopic view of blue bacteria"/>
    <polygon points="0,0 192,0 0,160" fill="var(--brand)"/>
  </svg>
  <div class="brand-mark"><span class="dot"></span>Cedar Ridge Labs</div>
  <h1 class="page-title" style="top:155px">ANTIBIOTIC <span>RESISTANCE GENE</span></h1>
  <div class="features" style="top:176px">
    <div class="feature"><svg viewBox="0 0 22 22"><rect x="2" y="14" width="3" height="6" fill="#1f74c6"/><rect x="7" y="11" width="3" height="9" fill="#1f74c6"/><rect x="12" y="8" width="3" height="12" fill="#1f74c6"/><rect x="17" y="5" width="3" height="15" fill="#1f74c6"/><circle cx="4" cy="4" r="3.2" fill="#333"/></svg><div><b>Cost effective</b> to help<br>maximize your lab's <b>profits</b></div></div>
    <div class="feature"><svg viewBox="0 0 22 22"><circle cx="11" cy="11" r="9" fill="#1f74c6"/><path d="M11 3v16M6 8h4M12 13h4" stroke="#fff" stroke-width="1.4"/></svg><div>Compatible with <b>ALL<br>PCR MACHINES</b></div></div>
    <div class="feature"><svg viewBox="0 0 22 22"><circle cx="11" cy="11" r="9" fill="none" stroke="#333" stroke-width="1.2" stroke-dasharray="3 1.5"/><circle cx="11" cy="11" r="6.5" fill="#1f74c6"/><path d="M11 7v4h3" stroke="#fff" stroke-width="1.4" fill="none"/></svg><div><b>&lt;45 minute</b> run time ensures<br><b>faster</b> turnaround times</div></div>
    <div class="feature"><svg viewBox="0 0 22 22"><path d="M6 10l4-4 3 3 6-6" stroke="#333" stroke-width="1.4" fill="none"/><circle cx="4" cy="17" r="2" fill="#1f74c6"/><circle cx="11" cy="17" r="2" fill="#1f74c6"/><circle cx="18" cy="17" r="2" fill="#1f74c6"/></svg><div><b>Highly demanded</b> targets to<br>make your lab <b>more appealing</b></div></div>
  </div>
  <div class="band" style="top:246px"><h2>12 TARGETS</h2><p>A provider's priority is ther patients. When you bring them more targets, you are providing them netter tools for treatment</p></div>
  <div class="content" style="top:295px">
    <div class="section-head">ABR</div>
    <ul class="list">
      <li>KPC - Carbapenem resistance</li><li>NDM - Carbapenem resistance</li><li>VIM - Carbapenem resistance</li><li>IMP - Carbapenem resistance</li><li>qnr - Quinolone resistance</li><li>vanB - Vancomycin resistance</li><li>OXA-48 - Carbapenem resistance</li><li>mecA/mecC - Methicillin resistance</li><li>CTX-M ESBL</li><li>sul - Sulfonamide resistance</li><li>vanA - Vancomycin resistance</li><li>dfrA - Trimethoprim resistance</li>
    </ul>
  </div>
  <div class="photo" style="position:absolute;left:169px;top:311px;width:84px;height:63px;background:linear-gradient(135deg,#6a5a3a,#d9a93a)" role="img" aria-label="Golden virus particle beside DNA strand"></div>
  <div class="photo" style="position:absolute;left:256px;top:311px;width:84px;height:63px;background:linear-gradient(135deg,#8fd6c9,#2c8f8a)" role="img" aria-label="Teal DNA helix illustration"></div>
  <div class="photo" style="position:absolute;left:169px;top:377px;width:84px;height:63px;background:linear-gradient(135deg,#0d3a33,#22a36a)" role="img" aria-label="Green glowing DNA and virus"></div>
  <div class="photo" style="position:absolute;left:256px;top:377px;width:84px;height:63px;background:linear-gradient(135deg,#d8dde0,#8e9aa2)" role="img" aria-label="Lab scientist holding a test tube"></div>
  <span class="pagenum"></span>
</section>

<!-- Page 2: Nail / Fungal -->
<section class="page page--nail">
  <svg class="hero" height="222" viewBox="0 0 362 222">
    <polygon points="140,0 362,0 362,162 100,70" fill="#c9d2dc" role="img" aria-label="Gloved hands treating a toenail"/>
    <polygon points="260,0 362,0 362,120 300,80" fill="#2a6fd0" opacity=".75"/>
    <polygon points="0,0 190,0 0,126" fill="var(--brand)"/>
  </svg>
  <div class="brand-mark"><span class="dot"></span>Cedar Ridge Labs</div>
  <h1 class="page-title" style="top:125px">NAIL/ <span>FUNGAL</span></h1>
  <div class="features" style="top:144px">
    <div class="feature"><svg viewBox="0 0 22 22"><rect x="2" y="14" width="3" height="6" fill="#1f74c6"/><rect x="7" y="11" width="3" height="9" fill="#1f74c6"/><rect x="12" y="8" width="3" height="12" fill="#1f74c6"/><rect x="17" y="5" width="3" height="15" fill="#1f74c6"/><circle cx="4" cy="4" r="3.2" fill="#333"/></svg><div><b>Cost effective</b> to help<br>maximize your lab's <b>profits</b></div></div>
    <div class="feature"><svg viewBox="0 0 22 22"><circle cx="11" cy="11" r="9" fill="#1f74c6"/><path d="M11 3v16M6 8h4M12 13h4" stroke="#fff" stroke-width="1.4"/></svg><div>Compatible with <b>ALL<br>PCR MACHINES</b></div></div>
    <div class="feature"><svg viewBox="0 0 22 22"><circle cx="11" cy="11" r="9" fill="none" stroke="#333" stroke-width="1.2" stroke-dasharray="3 1.5"/><circle cx="11" cy="11" r="6.5" fill="#1f74c6"/><path d="M11 7v4h3" stroke="#fff" stroke-width="1.4" fill="none"/></svg><div><b>&lt;45 minute</b> run time ensures<br><b>faster</b> turnaround times</div></div>
    <div class="feature"><svg viewBox="0 0 22 22"><path d="M6 10l4-4 3 3 6-6" stroke="#333" stroke-width="1.4" fill="none"/><circle cx="4" cy="17" r="2" fill="#1f74c6"/><circle cx="11" cy="17" r="2" fill="#1f74c6"/><circle cx="18" cy="17" r="2" fill="#1f74c6"/></svg><div><b>Highly demanded</b> targets to<br>make your lab <b>more appealing</b></div></div>
  </div>
  <div class="band" style="top:222px"><h2>18 TARGETS</h2><p>A provider's #1 priority is their patients. When you bring them more targets, you are providing them better tools for treatment</p></div>
  <div class="content" style="top:270px;left:23px">
    <div class="section-head">FUNGI</div>
    <div style="display:flex;gap:16px">
      <ul class="list" style="width:107px">
        <li style="line-height:16.3px">Microsporum gypseum</li><li style="line-height:16.3px">Microsporum canis/audouinii</li><li style="line-height:16.3px">Trichophyton spp</li><li style="line-height:16.3px">Malassezia furfur</li><li style="line-height:16.3px">Malassezia sympodialis</li><li style="line-height:16.3px">Candida krusei</li><li style="line-height:16.3px">Candida albicans</li><li style="line-height:16.3px">Candida glabrata</li><li style="line-height:16.3px">Candida parapsilosis</li>
      </ul>
      <ul class="list">
        <li style="line-height:16.3px">Candida auris</li><li style="line-height:16.3px">Aspergillus niger</li><li style="line-height:16.3px">Aspergillus flavus</li><li style="line-height:16.3px">Aspergillus fumigatus</li><li style="line-height:16.3px">Aspergillus terreus</li><li style="line-height:16.3px">Epidermophyton floccosum</li><li style="line-height:16.3px">Fusarium oxysporum</li><li style="line-height:16.3px">Trichosporon asahii</li><li style="line-height:16.3px">Trichosporon mucoides</li>
      </ul>
    </div>
  </div>
  <div class="photo" style="position:absolute;left:257px;top:280px;width:84px;height:49px;background:linear-gradient(135deg,#f4ede8,#e3c8b8)" role="img" aria-label="Bare feet on white background"></div>
  <div class="photo" style="position:absolute;left:257px;top:332px;width:84px;height:49px;background:linear-gradient(135deg,#b5aca4,#e0c7b6)" role="img" aria-label="Person touching sore feet"></div>
  <div class="photo" style="position:absolute;left:257px;top:384px;width:84px;height:49px;background:linear-gradient(135deg,#f1e4dc,#d69f86)" role="img" aria-label="Close view of a foot and toes"></div>
  <span class="pagenum"></span>
</section>

<!-- Page 3: Urinary Tract Infection -->
<section class="page page--uti">
  <svg class="hero" height="205" viewBox="0 0 362 205">
    <polygon points="160,0 362,0 362,178 113,57" fill="#0c2740" role="img" aria-label="Glowing wireframe illustration of a bladder"/>
    <ellipse cx="250" cy="40" rx="36" ry="32" fill="#1c5b8a" opacity=".7"/>
    <polygon points="0,0 181,0 0,132" fill="var(--brand)"/>
  </svg>
  <div class="brand-mark"><span class="dot"></span>Cedar Ridge Labs</div>
  <h1 class="page-title" style="top:123px">URINARY <span>TRACT INFECTION</span></h1>
  <div class="features" style="top:146px">
    <div class="feature"><svg viewBox="0 0 22 22"><rect x="2" y="14" width="3" height="6" fill="#1f74c6"/><rect x="7" y="11" width="3" height="9" fill="#1f74c6"/><rect x="12" y="8" width="3" height="12" fill="#1f74c6"/><rect x="17" y="5" width="3" height="15" fill="#1f74c6"/><circle cx="4" cy="4" r="3.2" fill="#333"/></svg><div><b>Cost effective</b> to help<br>maximize your lab's <b>profits</b></div></div>
    <div class="feature"><svg viewBox="0 0 22 22"><circle cx="11" cy="11" r="9" fill="#1f74c6"/><path d="M11 3v16M6 8h4M12 13h4" stroke="#fff" stroke-width="1.4"/></svg><div>Compatible with<br><b>ALL PCR MACHINES</b></div></div>
    <div class="feature"><svg viewBox="0 0 22 22"><circle cx="11" cy="11" r="9" fill="none" stroke="#333" stroke-width="1.2" stroke-dasharray="3 1.5"/><circle cx="11" cy="11" r="6.5" fill="#1f74c6"/><path d="M11 7v4h3" stroke="#fff" stroke-width="1.4" fill="none"/></svg><div><b>&lt;45 minute</b> run time ensures<br><b>faster</b> turnaround times</div></div>
    <div class="feature"><svg viewBox="0 0 22 22"><path d="M6 10l4-4 3 3 6-6" stroke="#333" stroke-width="1.4" fill="none"/><circle cx="4" cy="17" r="2" fill="#1f74c6"/><circle cx="11" cy="17" r="2" fill="#1f74c6"/><circle cx="18" cy="17" r="2" fill="#1f74c6"/></svg><div><b>Highly demanded</b> targets to<br>make your lab <b>more appealing</b></div></div>
  </div>
  <div class="band" style="top:205px"><h2>28 TARGETS</h2><p>A provider's #1 priority is their patients. When you bring them more targets, you are providing them better tools for treatment.</p></div>
  <div class="content" style="top:258px">
    <div class="section-head">BACTERIA</div>
    <div style="display:flex;gap:12px">
      <ul class="list" style="width:111px">
        <li>Escherichia coli</li><li>Streptococcus agalactiae</li><li>Klebsiella oxytoca</li><li>Staphylococcus saprophyticus</li><li>Serratia marcescens</li><li>Proteus mirabilis</li><li>Aerococcus urinae</li><li>Treponema pallidum</li><li>Enterobacter cloacae</li><li>Pseudomonas aeruginosa</li><li>Citrobacter freundii</li>
      </ul>
      <ul class="list">
        <li>Klebsiella aerogenes</li><li>Klebsiella pneumoniae</li><li>Morganella morganii</li><li>Corynebacterium urealyticum</li><li>Enterococcus faecium</li><li>Enterococcus faecalis</li><li>Acinetobacter baumannii</li><li>Proteus vulgaris</li><li>Staphylococcus aureus</li><li>Ureplasma</li><li>Providencia stuartii</li>
      </ul>
    </div>
    <div class="section-head" style="margin-top:1px">FUNGI</div>
    <div style="display:flex;gap:12px">
      <ul class="list" style="width:111px"><li>Candida parapsilosis</li><li>Candida glabrata</li><li>Candida auris</li></ul>
      <ul class="list"><li>Candida tropicalis</li><li>Candida krusei</li><li>Candida albicans</li></ul>
    </div>
  </div>
  <div class="photo" style="position:absolute;left:257px;top:259px;width:84px;height:55px;background:linear-gradient(135deg,#3b4fa8,#c8b7e6)" role="img" aria-label="Digital bladder illustration in blue and violet"></div>
  <div class="photo" style="position:absolute;left:257px;top:317px;width:84px;height:55px;background:linear-gradient(135deg,#cfe6f3,#2a7fc1)" role="img" aria-label="Glowing bladder above a hand"></div>
  <div class="photo" style="position:absolute;left:257px;top:375px;width:84px;height:55px;background:linear-gradient(180deg,#1a44c9,#f2a21a)" role="img" aria-label="Heat map illustration of a bladder"></div>
  <span class="pagenum"></span>
</section>

<!-- Page 4: Wound / Sepsis -->
<section class="page page--wound">
  <svg class="hero" height="213" viewBox="0 0 362 213">
    <polygon points="150,0 362,0 362,175 120,80" fill="#d3dbe2" role="img" aria-label="Gloved hands examining skin on an arm"/>
    <polygon points="250,10 330,0 362,60 300,90" fill="#2a6fd0" opacity=".75"/>
    <polygon points="0,0 190,0 0,128" fill="var(--brand)"/>
  </svg>
  <div class="brand-mark"><span class="dot"></span>Cedar Ridge Labs</div>
  <h1 class="page-title" style="top:124px">WOUND/ <span>SEPSIS</span></h1>
  <div class="features" style="top:145px">
    <div class="feature"><svg viewBox="0 0 22 22"><rect x="2" y="14" width="3" height="6" fill="#1f74c6"/><rect x="7" y="11" width="3" height="9" fill="#1f74c6"/><rect x="12" y="8" width="3" height="12" fill="#1f74c6"/><rect x="17" y="5" width="3" height="15" fill="#1f74c6"/><circle cx="4" cy="4" r="3.2" fill="#333"/></svg><div><b>Cost effective</b> to help<br>maximize your lab's <b>profits</b></div></div>
    <div class="feature"><svg viewBox="0 0 22 22"><circle cx="11" cy="11" r="9" fill="#1f74c6"/><path d="M11 3v16M6 8h4M12 13h4" stroke="#fff" stroke-width="1.4"/></svg><div>Compatible with<br><b>ALL PCR MACHINES</b></div></div>
    <div class="feature"><svg viewBox="0 0 22 22"><circle cx="11" cy="11" r="9" fill="none" stroke="#333" stroke-width="1.2" stroke-dasharray="3 1.5"/><circle cx="11" cy="11" r="6.5" fill="#1f74c6"/><path d="M11 7v4h3" stroke="#fff" stroke-width="1.4" fill="none"/></svg><div><b>&lt;45 minute</b> run time ensures<br><b>faster</b> turnaround times</div></div>
    <div class="feature"><svg viewBox="0 0 22 22"><path d="M6 10l4-4 3 3 6-6" stroke="#333" stroke-width="1.4" fill="none"/><circle cx="4" cy="17" r="2" fill="#1f74c6"/><circle cx="11" cy="17" r="2" fill="#1f74c6"/><circle cx="18" cy="17" r="2" fill="#1f74c6"/></svg><div><b>Highly demanded</b> targets to<br>make your lab <b>more appealing</b></div></div>
  </div>
  <div class="band" style="top:213px"><h2>28 TARGETS</h2><p>A provider's #1 priority is their patients. When you bring them more targets, you are providing them better tools for treatment.</p></div>
  <div class="content" style="top:261px">
    <div style="display:flex;gap:22px">
      <div style="width:113px">
        <div class="section-head">BACTERIA</div>
        <ul class="list">
          <li>Escherichia coli</li><li>Streptococcus agalactiae</li><li>Klebsiella oxytoca</li><li>Staphylococcus saprophyticus</li><li>Pseudomonas aeruginosa</li><li>Staphylococcus haemolyticus</li><li>Enterococcus faecium</li><li>Enterococcus faecalis</li><li>Acinetobacter calcoaceticus</li><li>baumannii complex</li><li>Klebsiella aerogenes</li><li>Klebsiella pneumoniae</li><li>Staphylococcus aureus</li><li>Streptococcus pyogenes</li><li>Streptococcus pneumoniae</li>
        </ul>
      </div>
      <div>
        <div class="section-head">FUNGI</div>
        <ul class="list">
          <li>Candida krusei</li><li>Candida tropicalis</li><li>Candida glabrata</li><li>Candida parapsilosis</li><li>Candida albicans</li><li>Fusarium solani</li><li>Microsporum spp</li><li>Trichophyton spp</li>
        </ul>
        <div class="section-head" style="margin-top:8px">ANTIMICROBIAL<br>RESISTANCE</div>
        <p class="small-note">Methicillin Resistance (MecA+C)</p>
        <div class="section-head" style="margin-top:8px">Viruses</div>
        <p class="small-note">Herpes Simplex Virus 1<br>HerpesSimplex Virus 2</p>
      </div>
    </div>
  </div>
  <div class="photo" style="position:absolute;left:257px;top:262px;width:84px;height:53px;background:linear-gradient(135deg,#3b7fd6,#7a3a2e)" role="img" aria-label="Gloved hand treating a wound"></div>
  <div class="photo" style="position:absolute;left:257px;top:318px;width:84px;height:53px;background:linear-gradient(135deg,#2f6fc8,#e8c9c0)" role="img" aria-label="Clinician bandaging a patient's arm"></div>
  <div class="photo" style="position:absolute;left:257px;top:374px;width:84px;height:53px;background:linear-gradient(135deg,#e9e7e2,#2e6fc7)" role="img" aria-label="Gloved hands with sample vials"></div>
  <span class="pagenum"></span>
</section>

</body>
</html>
```